Business Card Design Project

We require business cards for "Venoth". We are composed of elite prior military personnel. Our goal is to provide site security for premium businesses who want on the most professional of agents on their premises. Additionally, we will provide executive protection for individuals who require professionalism, flexibility, and dedication

We want this business card to communicate professionalism, dependability, strength. However, we are not an overtly tactical agency and do not want to intimidate our clients personnel or their client. We want to give them a sense of security.
Updates

At the request of one of the designers I've listed the appropriate text that should appear on the card. Please feel free to arrange it in a creative and professional manor.

I've also uploaded a .png file of the triangle logo with no text. Please feel free to incorporate this into your designs.

ThanksĀ 

Target Market(s)

Premium businesses, executives, celebrities, and governments.

Industry/Entity Type

Security

Requirements
Must have
• Text Info that will go on the card. It does not have to be in this order:
Name
Title
Office Phone Number
Cell Phone Number
Email
Website
Mailing Address
Nice to have
• On the back I'd like to see the triangle portion of the logo displayed in a creative way that leaves enough room to write down information if needed.
Should not have
• - Weapons, Globes, or Shields. Every rent-a-cop company has that, and that's not what we are.

```html
<!DOCTYPE html>
<html lang="en">
<head>
<meta charset="utf-8">
<title>Venoth Business Card – Front and Back</title>
<link rel="stylesheet" href="https://fonts.googleapis.com/css2?family=Open+Sans:wght@400;600;700;800&display=swap">
<style>
  :root {
    --page-bg: #e9ebee;
    --label-bg: #050505;
    --label-text: #ffffff;
    --ink-dark: #2b2b2d;
    --blue-light: #2ea3df;
    --blue-mid: #1e7dc2;
    --blue-deep: #164a8a;
    --paper: #ffffff;
    --paper-shade: #dfe2e6;
    --rule-grey: #8e8e8e;
    --white: #ffffff;
  }
  * { box-sizing: border-box; margin: 0; padding: 0; }
  html, body {
    width: 1200px;
    height: 2499px;
    overflow: hidden;
  }
  body {
    background: var(--page-bg);
    font-family: "Open Sans", Arial, sans-serif;
    display: flex;
    flex-direction: column;
    justify-content: center;
  }
  .side-label {
    height: 88px;
    background: var(--label-bg);
    color: var(--label-text);
    font-weight: 600;
    font-size: 60px;
    line-height: 88px;
    text-align: right;
    padding-right: 22px;
    letter-spacing: 1px;
  }
  .card {
    position: relative;
    width: 1200px;
    height: 715px;
    overflow: hidden;
  }

  /* Front */
  .card-front .brand-band {
    height: 250px;
    background: radial-gradient(ellipse at 50% 40%, var(--paper) 55%, var(--paper-shade) 100%);
    display: flex;
    align-items: center;
    justify-content: center;
    gap: 34px;
  }
  .brand-dot {
    width: 110px;
    height: 110px;
    border-radius: 50%;
    background: var(--blue-mid);
  }
  .brand-name {
    font-weight: 800;
    font-size: 150px;
    color: var(--ink-dark);
    letter-spacing: 4px;
    line-height: 1;
  }
  .card-front .info-band {
    position: relative;
    height: 465px;
    background: linear-gradient(180deg, var(--blue-light) 0%, var(--blue-mid) 45%, var(--blue-deep) 100%);
    color: var(--white);
    padding: 20px 0 0 112px;
  }
  .person-name {
    font-weight: 400;
    font-size: 56px;
    line-height: 1.1;
  }
  .person-title {
    font-size: 26px;
    line-height: 1.3;
    margin-bottom: 28px;
  }
  .contact-row {
    display: flex;
    align-items: center;
    gap: 34px;
    margin-bottom: 30px;
    font-size: 27px;
    line-height: 1.32;
  }
  .contact-row svg { width: 48px; height: 48px; flex: none; }
  .faint-brand {
    position: absolute;
    right: 88px;
    top: 290px;
    font-weight: 800;
    font-size: 74px;
    color: var(--white);
    opacity: 0.16;
    letter-spacing: 2px;
  }

  /* Back */
  .card-back { background: radial-gradient(ellipse at 50% 70%, var(--paper) 50%, var(--paper-shade) 100%); }
  .card-back .dome { position: absolute; inset: 0 0 auto 0; width: 1200px; height: 440px; }
  .card-back .back-brand {
    position: absolute;
    top: 150px;
    left: 0;
    width: 1200px;
    text-align: center;
    font-weight: 800;
    font-size: 150px;
    line-height: 1;
    color: var(--white);
    letter-spacing: 4px;
  }
  .note-lines {
    position: absolute;
    left: 187px;
    top: 465px;
    width: 835px;
    list-style: none;
  }
  .note-lines li {
    height: 4px;
    background: var(--rule-grey);
    margin-bottom: 53px;
  }
</style>
</head>
<body>

  <div class="side-label">FRONT</div>
  <section class="card card-front">
    <div class="brand-band">
      <span class="brand-dot"></span>
      <span class="brand-name">VENOTH</span>
    </div>
    <div class="info-band">
      <h1 class="person-name">NAME HERE</h1>
      <p class="person-title">TITLE HERE</p>

      <div class="contact-row">
        <svg viewBox="0 0 24 24" aria-hidden="true"><path fill="#fff" d="M6.6 10.8a15.2 15.2 0 0 0 6.6 6.6l2.2-2.2a1 1 0 0 1 1-.25 11.4 11.4 0 0 0 3.6.57 1 1 0 0 1 1 1V20a1 1 0 0 1-1 1A17 17 0 0 1 3 4a1 1 0 0 1 1-1h3.5a1 1 0 0 1 1 1c0 1.25.2 2.45.57 3.6a1 1 0 0 1-.25 1z"/></svg>
        <p>OFFICE: 000.000.0000<br>CELL: 000.000.0000</p>
      </div>

      <div class="contact-row">
        <svg viewBox="0 0 24 24" aria-hidden="true" fill="none" stroke="#fff" stroke-width="1.8"><circle cx="12" cy="12" r="9.5"/><ellipse cx="12" cy="12" rx="4.2" ry="9.5"/><path d="M2.5 12h19M4 7h16M4 17h16"/></svg>
        <p>EMAIL: YOUREMAILHERE@VENOTH.COM<br>WEBSITE: WWW.VENOTH.COM</p>
      </div>

      <div class="contact-row">
        <svg viewBox="0 0 24 24" aria-hidden="true" fill="none" stroke="#fff" stroke-width="2"><circle cx="12" cy="12" r="10"/><path d="M8 16l2.5-6L16 8l-2.5 6z" fill="#fff"/></svg>
        <p>ADDRESS: 1234 ANWHERE BLV.<br>CITY, STATE, ZIP CODE.</p>
      </div>

      <span class="faint-brand">VENOTH</span>
    </div>
  </section>

  <div class="side-label">BACK</div>
  <section class="card card-back">
    <svg class="dome" viewBox="0 0 1200 440" aria-hidden="true">
      <defs>
        <linearGradient id="domeFill" x1="0" y1="0" x2="0" y2="1">
          <stop offset="0" stop-color="#2b97d6"/>
          <stop offset="0.55" stop-color="#1d6fb6"/>
          <stop offset="1" stop-color="#174d92"/>
        </linearGradient>
      </defs>
      <path d="M0 0H1200V330Q600 500 0 330Z" fill="url(#domeFill)"/>
    </svg>
    <div class="back-brand">VENOTH</div>
    <ul class="note-lines">
      <li></li><li></li><li></li><li></li>
    </ul>
  </section>

</body>
</html>
```